Crestmoor Air Global Business Card

I would like a professional business card designed. The plane that is being used is a Skyvane Aero Marshal 2400. Our primary business colors would be navy blue and light blue. This is a charter plane for hire. Our clients range from business people to vacation goers. A website is currently under development and two of the primary pictures being used will be attached. The pictures don't need to be used in the business card design, but could be used for inspiration and reference. We will need our P.O. Box address on the card and personal information (Name, cell number, email address, and website address (www.crestmoorairglobal.example)) Thanks! God Bless!
Updates

The contact info for the back of the card: Dale Whitcombe Cell: 555.014.2867 Email: dwhitcombe@crestmoorairglobal.example

Target Market(s)

Business people

Industry/Entity Type

Business

Contact Information for Business Card

This will be on a standard square cornered business card.

Requirements
Must have
• Professional look

```html
<!DOCTYPE html>
<html lang="en">
<head>
<meta charset="utf-8">
<title>Crestmoor Air Global – Business Card</title>
<link rel="stylesheet" href="https://fonts.googleapis.com/css2?family=Cinzel:wght@500&family=Jost:wght@300&display=swap">
<style>
  :root {
    --sky-deep: #1f5fc9;
    --sky-mid: #2f7be6;
    --sky-light: #4a95ee;
    --cloud-warm: #e8c48c;
    --cloud-shadow: #8a7a6a;
    --navy: #03438c;
    --accent-blue: #36a9e1;
    --white: #ffffff;
  }
  * { margin: 0; padding: 0; box-sizing: border-box; }
  html, body { width: 1084px; height: 1200px; overflow: hidden; background: var(--navy); }
  .card-sheet { position: relative; width: 1084px; height: 1200px; }

  .front-side {
    position: absolute; left: 0; top: 0; width: 1084px; height: 603px;
    background:
      radial-gradient(ellipse 420px 260px at 120px 470px, var(--cloud-warm) 0%, rgba(232,196,140,0.75) 40%, rgba(232,196,140,0) 100%),
      radial-gradient(ellipse 380px 120px at 480px 570px, rgba(214,180,130,0.85) 0%, rgba(214,180,130,0) 100%),
      radial-gradient(ellipse 300px 200px at 80px 580px, var(--cloud-shadow) 0%, rgba(138,122,106,0) 100%),
      linear-gradient(180deg, var(--sky-deep) 0%, var(--sky-mid) 45%, var(--sky-light) 100%);
  }
  .brand-title {
    position: absolute; left: 81px;
    font-family: "Cinzel", serif; font-weight: 500;
    color: var(--white); white-space: nowrap;
    font-size: 50px; letter-spacing: 1px;
  }
  .front-side .brand-title { top: 178px; text-shadow: 2px 3px 4px rgba(0,0,0,0.45); }
  .website {
    position: absolute; right: 33px; top: 532px;
    font-family: "Jost", sans-serif; font-weight: 300;
    font-size: 40px; color: var(--white);
    text-shadow: 1px 2px 3px rgba(0,0,0,0.4);
  }

  .back-side {
    position: absolute; left: 0; top: 603px; width: 1084px; height: 597px;
    background: var(--navy);
  }
  .back-side .brand-title { left: 70px; top: 117px; }
  .accent-bar {
    position: absolute; right: 0; top: 305px; width: 44px; height: 225px;
    background: var(--accent-blue);
  }
  .contact-block {
    position: absolute; right: 81px; top: 360px;
    font-family: "Jost", sans-serif; font-weight: 300;
    color: var(--white); text-align: right;
  }
  .contact-line {
    display: flex; align-items: center; justify-content: flex-end;
    font-size: 45px; line-height: 60px; height: 60px;
  }
  .contact-line.email { font-size: 40px; }
  .contact-icon { width: 54px; height: 54px; margin-right: 10px; flex: none; }
</style>
</head>
<body>
<div class="card-sheet">
  <section class="front-side" role="img" aria-label="Photograph of a twin-engine charter plane flying in a blue sky above golden sunlit clouds">
    <div class="brand-title">Crestmoor Air Global</div>
    <div class="website">www.crestmoorairglobal.example</div>
  </section>

  <section class="back-side">
    <div class="brand-title">Crestmoor Air Global</div>
    <div class="accent-bar"></div>
    <div class="contact-block">
      <div class="contact-line name">Dale Whitcombe</div>
      <div class="contact-line phone">
        <svg class="contact-icon" viewBox="0 0 54 54" aria-hidden="true">
          <circle cx="27" cy="27" r="27" fill="#36a9e1"/>
          <path d="M19 14c2-1 3 0 4 2l2 4c1 2 0 3-1 4l-1 1c1 3 4 6 7 7l1-1c1-1 2-2 4-1l4 2c2 1 3 2 2 4l-1 2c-1 2-4 3-7 2-7-2-13-8-15-15-1-3 0-6 1-7z" fill="#03438c"/>
        </svg>
        Cell: + 555.014.2867
      </div>
      <div class="contact-line email">
        <svg class="contact-icon" viewBox="0 0 54 54" aria-hidden="true">
          <circle cx="27" cy="27" r="27" fill="#36a9e1"/>
          <rect x="15" y="18" width="24" height="18" fill="#03438c"/>
          <path d="M15 18l12 10 12-10M15 36l9-8M39 36l-9-8" fill="none" stroke="#36a9e1" stroke-width="2"/>
        </svg>
        dwhitcombe@crestmoorairglobal.example
      </div>
    </div>
  </section>
</div>
</body>
</html>
```